Electronic hardware design and manufacturer needing a new business card design.

We need a new business card design consisting of a double sided design adhering to brand and logo guidelines attached. I also want to incorporate something that recognizes our 25th year in business ("EST 2001" or something like that....).

```html
<!DOCTYPE html>
<html lang="en">
<head>
<meta charset="utf-8">
<title>Kestrel Telemetry Corp. – Business Card</title>
<link rel="stylesheet" href="https://fonts.googleapis.com/css2?family=Open+Sans:wght@400;600;700;800&display=swap">
<style>
  :root {
    --stage: #161616;
    --card-top: #14475d;
    --card-bottom: #0b3244;
    --gold: #e3aa1e;
    --orange: #e8761f;
    --green: #62c22a;
    --navy: #0b2433;
    --white: #ffffff;
    --muted: #c9d4da;
  }
  * { margin: 0; padding: 0; box-sizing: border-box; }
  html, body { width: 1200px; height: 963px; overflow: hidden; }
  body {
    background: var(--stage);
    font-family: "Open Sans", Arial, sans-serif;
    color: var(--white);
    position: relative;
  }
  .card {
    position: absolute;
    left: 290px;
    width: 620px;
    height: 354px;
    border-radius: 18px;
    background: linear-gradient(160deg, var(--card-top), var(--card-bottom));
    overflow: hidden;
  }
  .card--front { top: 92px; }
  .card--back { top: 516px; }

  /* Brand mark */
  .brand {
    position: absolute;
    right: 40px;
    display: flex;
    align-items: center;
    gap: 14px;
  }
  .brand__dot {
    width: 50px; height: 50px;
    border-radius: 50%;
    background: var(--gold);
    flex: none;
  }
  .brand__name {
    font-weight: 800;
    font-size: 27px;
    line-height: 1.05;
    letter-spacing: 0.5px;
    text-transform: uppercase;
    color: var(--white);
    white-space: nowrap;
  }
  .card--front .brand { top: 70px; }
  .card--back .brand { top: 48px; }

  /* Front */
  .person { position: absolute; left: 42px; top: 150px; }
  .person__name { font-size: 29px; font-weight: 700; color: var(--gold); line-height: 1.1; }
  .person__role { font-size: 17px; font-weight: 400; color: var(--white); margin-top: 2px; }
  .rule {
    position: absolute;
    left: 32px; right: 32px; top: 222px;
    height: 1.5px;
    background: var(--white);
  }
  .contacts { position: absolute; left: 42px; top: 236px; list-style: none; }
  .contacts li {
    display: flex; align-items: center; gap: 12px;
    font-size: 16px; height: 27px; white-space: nowrap;
  }
  .contacts svg { width: 17px; height: 17px; flex: none; }
  .address {
    position: absolute; right: 38px; bottom: 26px;
    text-align: right; font-size: 16px; line-height: 1.45; white-space: nowrap;
  }

  /* Back: anniversary badge */
  .anniversary { position: absolute; left: 36px; top: 22px; width: 240px; height: 140px; }
  .anniversary__est {
    position: absolute; left: 0; top: 62px;
    font-size: 12px; color: var(--white); white-space: nowrap;
  }
  .anniversary__number {
    position: absolute; left: 78px; top: -8px;
    font-size: 104px; font-weight: 800; color: var(--gold);
    line-height: 1; letter-spacing: -4px;
  }
  .anniversary__suffix {
    position: absolute; left: 200px; top: 6px;
    font-size: 32px; font-weight: 800; color: var(--orange); line-height: 1;
  }
  .anniversary__label {
    position: absolute; left: 84px; top: 108px;
    font-size: 13px; font-weight: 700; color: var(--orange);
    text-transform: uppercase; white-space: nowrap;
  }

  /* Back: product line */
  .products { position: absolute; left: 26px; right: 26px; top: 180px; }
  .products__row { display: flex; gap: 10px; margin-bottom: 16px; }
  .products__row--first .product { flex: 1; }
  .products__row--second { justify-content: center; }
  .product {
    display: flex; align-items: center; gap: 8px;
    border: 1.5px dashed var(--muted);
    padding: 7px 10px 7px 8px;
    border-radius: 3px;
  }
  .product__mark { width: 28px; height: 28px; border-radius: 6px; flex: none; }
  .product__name { font-size: 21px; font-weight: 700; line-height: 1; white-space: nowrap; }
  .product__desc {
    font-size: 7.5px; font-weight: 600; text-transform: uppercase;
    color: var(--muted); letter-spacing: 0.3px; margin-top: 3px; white-space: nowrap;
  }
  .product--ranger .product__mark { background: var(--green); }
  .product--ranger .product__name { color: var(--green); }
  .product--beacon .product__mark { background: var(--orange); }
  .product--beacon .product__name { color: var(--orange); }
  .product--tracer .product__mark { background: var(--gold); }
  .product--tracer .product__name { color: var(--gold); }
  .product--scope .product__mark { background: var(--navy); }
  .product--scope .product__name { color: var(--white); }
  .product--bridge .product__mark { background: var(--navy); }
  .product--bridge .product__name { color: var(--white); }
</style>
</head>
<body>

<section class="card card--front" aria-label="Business card front">
  <div class="brand">
    <span class="brand__dot"></span>
    <span class="brand__name">Kestrel<br>Telemetry Corp.</span>
  </div>

  <div class="person">
    <p class="person__name">Daniel Mercer</p>
    <p class="person__role">Owner</p>
  </div>

  <div class="rule"></div>

  <ul class="contacts">
    <li>
      <svg viewBox="0 0 24 24" aria-hidden="true"><path fill="var(--orange)" d="M6.6 10.8a15.1 15.1 0 0 0 6.6 6.6l2.2-2.2a1 1 0 0 1 1-.25 11.4 11.4 0 0 0 3.6.57 1 1 0 0 1 1 1V20a1 1 0 0 1-1 1A17 17 0 0 1 3 4a1 1 0 0 1 1-1h3.5a1 1 0 0 1 1 1c0 1.25.2 2.45.57 3.57a1 1 0 0 1-.25 1z"/></svg>
      044-870 312 655
    </li>
    <li>
      <svg viewBox="0 0 24 24" aria-hidden="true"><path fill="var(--orange)" d="M2 5h20v14H2z"/><path fill="none" stroke="var(--card-bottom)" stroke-width="1.6" d="M2 5l10 8 10-8"/></svg>
      daniel@kestreltel.com
    </li>
    <li>
      <svg viewBox="0 0 24 24" aria-hidden="true"><circle cx="12" cy="12" r="9.5" fill="none" stroke="var(--orange)" stroke-width="2"/><path fill="none" stroke="var(--orange)" stroke-width="1.6" d="M2.5 12h19M12 2.5c3 3 3 16 0 19M12 2.5c-3 3-3 16 0 19"/></svg>
      www.kestreltel.com
    </li>
  </ul>

  <p class="address">118, Ironwood Road, Suite 4<br>30917, Northvale</p>
</section>

<section class="card card--back" aria-label="Business card back">
  <div class="anniversary">
    <span class="anniversary__est">(EST 2001)</span>
    <span class="anniversary__number">25</span>
    <span class="anniversary__suffix">th</span>
    <span class="anniversary__label">Year in Business</span>
  </div>

  <div class="brand">
    <span class="brand__dot"></span>
    <span class="brand__name">Kestrel<br>Telemetry Corp.</span>
  </div>

  <div class="products">
    <div class="products__row products__row--first">
      <div class="product product--ranger">
        <span class="product__mark"></span>
        <div><p class="product__name">Ranger</p><p class="product__desc">Plunger lift controller</p></div>
      </div>
      <div class="product product--beacon">
        <span class="product__mark"></span>
        <div><p class="product__name">Beacon</p><p class="product__desc">Plunger arrival sensor</p></div>
      </div>
      <div class="product product--tracer">
        <span class="product__mark"></span>
        <div><p class="product__name">Tracer</p><p class="product__desc">Plunger velocity sensor</p></div>
      </div>
    </div>
    <div class="products__row products__row--second">
      <div class="product product--scope">
        <span class="product__mark"></span>
        <div><p class="product__name">Scope</p><p class="product__desc">Device management</p></div>
      </div>
      <div class="product product--bridge">
        <span class="product__mark"></span>
        <div><p class="product__name">Bridge™</p><p class="product__desc">Device connection</p></div>
      </div>
    </div>
  </div>
</section>

</body>
</html>
```